Verostel business card

Business card for sustainable investment company called "Verostel". Verostel is an exchange platform selling carbon credits between buyers and sellers. Carbon Credits are an environmental commodity for reducing global carbon emissions.

the card should obviously have our logo and the theme should be sustainability/environment mixed with a trading platform.

Contact Information for Business Card

Logo, Name, Title, Phone, Email

Colors
0054AA
0677BA
7BADD7
CADEEF
E8F1F8
0094D4
00A9DD
6FCCEA
C7EBF8
E9F6FB
00AB8E
00BBA5
67D7C9
C6EFE9
E9F9F6
59FF00
82FF00
B8FF75
E3FFCB
F4FFEA

```html
<!DOCTYPE html>
<html lang="en">
<head>
<meta charset="utf-8">
<title>Verostel Business Card</title>
<link rel="stylesheet" href="https://fonts.googleapis.com/css2?family=Raleway:wght@500;700&display=swap">
<style>
  :root {
    --backdrop: #e6e8eb;
    --card-white: #ffffff;
    --ink-navy: #1d2a44;
    --ink-grey: #4a4f57;
    --teal-light: #62c9de;
    --sky: #36c2e9;
    --ocean: #3aa3dd;
    --deep-blue: #4169b6;
  }
  * { box-sizing: border-box; margin: 0; padding: 0; }
  html, body {
    width: 1200px; height: 588px; overflow: hidden;
    background: var(--backdrop);
    font-family: "Raleway", sans-serif;
  }
  .canvas { position: relative; width: 1200px; height: 588px; }
  .card {
    position: absolute;
    width: 487px; height: 287px;
    border-radius: 24px;
    overflow: hidden;
  }
  .card-front {
    left: 87px; top: 141px;
    background: linear-gradient(90deg, var(--teal-light) 0%, var(--sky) 30%, var(--ocean) 55%, var(--deep-blue) 100%);
    display: flex; align-items: center; justify-content: center;
  }
  .card-back {
    left: 622px; top: 143px;
    background: var(--card-white);
  }
  .wordmark {
    display: flex; align-items: center; gap: 12px;
    font-weight: 700; letter-spacing: 0.5px;
  }
  .wordmark-dot { width: 34px; height: 34px; border-radius: 50%; }
  .card-front .wordmark { color: var(--card-white); font-size: 40px; margin-top: -6px; }
  .card-front .wordmark-dot { background: var(--card-white); width: 40px; height: 40px; }
  .card-back .wordmark {
    position: absolute; left: 30px; top: 128px;
    color: var(--ink-navy); font-size: 29px;
  }
  .card-back .wordmark-dot { background: var(--ocean); }
  .divider {
    position: absolute; left: 260px; top: 96px;
    width: 1.5px; height: 96px; background: var(--ink-navy);
  }
  .contact-block { position: absolute; left: 275px; top: 92px; }
  .person-name { font-size: 19px; font-weight: 700; color: var(--ink-navy); letter-spacing: 0.3px; }
  .person-title { font-size: 13px; font-weight: 500; color: var(--ink-grey); margin-top: 2px; }
  .contact-list { list-style: none; margin-top: 12px; }
  .contact-list li {
    display: flex; align-items: center; gap: 5px;
    font-size: 13px; font-weight: 500; color: var(--ink-grey);
    height: 18px;
  }
  .contact-list svg { width: 11px; height: 11px; flex: none; }
  .accent-band {
    position: absolute; left: 0; bottom: 0; width: 100%; height: 11px;
    background: linear-gradient(90deg, var(--teal-light), var(--ocean) 50%, var(--deep-blue));
  }
</style>
</head>
<body>
<main class="canvas">
  <section class="card card-front" aria-label="Card front">
    <div class="wordmark"><span class="wordmark-dot"></span><span>VEROSTEL</span></div>
  </section>

  <section class="card card-back" aria-label="Card back">
    <div class="wordmark"><span class="wordmark-dot"></span><span>VEROSTEL</span></div>
    <div class="divider"></div>
    <div class="contact-block">
      <h1 class="person-name">MAREK OLUND</h1>
      <p class="person-title">President</p>
      <ul class="contact-list">
        <li>
          <svg viewBox="0 0 24 24" aria-hidden="true"><path fill="#3aa3dd" d="M6.6 10.8a15.1 15.1 0 0 0 6.6 6.6l2.2-2.2c.3-.3.7-.4 1-.2 1.1.4 2.3.6 3.6.6.6 0 1 .4 1 1V20c0 .6-.4 1-1 1A17 17 0 0 1 3 4c0-.6.4-1 1-1h3.5c.6 0 1 .4 1 1 0 1.3.2 2.5.6 3.6.1.3 0 .7-.2 1z"/></svg>
          555-014-2287
        </li>
        <li>
          <svg viewBox="0 0 24 24" aria-hidden="true"><rect x="2" y="5" width="20" height="14" rx="1.5" fill="#3aa3dd"/><path d="M3 6l9 7 9-7" fill="none" stroke="#fff" stroke-width="1.6"/></svg>
          marek.olund@verostel.com
        </li>
        <li>
          <svg viewBox="0 0 24 24" aria-hidden="true"><circle cx="12" cy="12" r="10" fill="#3aa3dd"/><path d="M2 12h20M12 2c3 3 3 17 0 20M12 2c-3 3-3 17 0 20" fill="none" stroke="#fff" stroke-width="1.4"/></svg>
          www.verostel.com
        </li>
      </ul>
    </div>
    <div class="accent-band"></div>
  </section>
</main>
</body>
</html>
```